Powerpoint Presentation Template

Kindly design a business class Powepoint Presentation template for our business use. Please stick to our company colours or even pictures as shown on our website and Logo

```html
<!DOCTYPE html>
<html lang="en">
<head>
<meta charset="utf-8">
<title>Meridian Properties – Presentation Template</title>
<link rel="stylesheet" href="https://fonts.googleapis.com/css2?family=Oswald:wght@400;500;600&family=Open+Sans:wght@400;600;700&display=swap">
<style>
:root{
  --maroon:#8a2a22;
  --maroon-dark:#6e1f19;
  --charcoal:#3b3735;
  --stage:#6f6a66;
  --ink:#333;
  --muted:#8a8a8a;
  --line:#d9d9d9;
  --paper:#ffffff;
}
*{box-sizing:border-box;margin:0;padding:0}
html,body{width:1200px;height:1120px;overflow:hidden;background:var(--stage)}
body{font-family:"Open Sans",sans-serif;color:var(--ink)}
.deck{display:grid;grid-template-columns:repeat(5,224px);grid-template-rows:repeat(7,144px);gap:16px;padding:8px}
.slide{position:relative;background:var(--paper);overflow:hidden}
.title{position:absolute;left:12px;top:11px;font:500 6.5px "Oswald",sans-serif;letter-spacing:.2px;color:#222;text-transform:uppercase}
.title.red{color:var(--maroon)}
.brand{position:absolute;right:10px;top:7px;text-align:center;line-height:1}
.brand b{display:block;font:600 5.5px "Oswald",sans-serif;color:var(--maroon);letter-spacing:.3px}
.brand i{font-style:normal;font-size:3.4px;color:var(--maroon)}
.brand.big b{font-size:11px}.brand.big i{font-size:6.5px}
.brand.white b,.brand.white i{color:#fff}
.foot{position:absolute;left:0;right:0;bottom:0;height:6px;border-top:.5px solid var(--line);font-size:2.6px;color:var(--muted);padding:1px 12px}
.foot::after{content:"Page 1";position:absolute;right:4px;top:1px;background:var(--maroon);color:#fff;padding:0 3px;font-size:2.4px}
.txt{font-size:3.2px;line-height:1.45;color:#777}
.ph{position:absolute;display:block}
.soil{background:linear-gradient(180deg,#9fb3c4 0%,#c9c2b5 30%,#b06a45 55%,#8a4a2c 100%)}
.bldg{background:linear-gradient(180deg,#a9c1d8 0%,#d9dfe3 40%,#9c7f6b 65%,#6b5a50 100%)}
.road{background:linear-gradient(180deg,#9fb6c7 0%,#7d8a6b 40%,#6a6d70 60%,#4d5054 100%)}
.pipe{background:linear-gradient(180deg,#c29572 0%,#a8653f 50%,#6f8fb0 75%,#8c5436 100%)}
.face{background:linear-gradient(180deg,#e8e2da 0%,#c9a68a 55%,#4a3c34 100%)}
.face2{background:linear-gradient(180deg,#eee5d8 0%,#d9b08a 50%,#b57a4e 100%)}
.suit{background:linear-gradient(180deg,#e0d8cf 0%,#c9a68a 35%,#27324a 60%,#1f2a3f 100%)}
.site{background:linear-gradient(180deg,#b8c4cc 0%,#8a7d6e 50%,#6b5e52 100%)}
.hand{background:linear-gradient(135deg,#e9e5e0 0%,#c8bfb4 50%,#4a4440 100%)}
.bullets{display:flex;gap:6px;font-size:2.6px;color:#555}
.bullets span::before{content:"";display:inline-block;width:2px;height:2px;border:.4px solid var(--maroon);margin-right:1.5px}
.btn{display:inline-block;background:var(--maroon-dark);color:#fff;font-size:2.6px;padding:1.5px 4px}
.ptitle{font:400 8px "Oswald",sans-serif;color:var(--maroon);letter-spacing:.2px}
.agenda-dark{position:absolute;left:0;top:0;bottom:0;width:100px;background:var(--charcoal);color:#fff;padding:50px 8px 0 16px}
.agenda-dark h3{font:500 6.5px "Oswald",sans-serif;margin-bottom:10px}
.agenda-dark .txt{color:#ddd}
.numbox{position:absolute;width:13px;height:13px;background:var(--maroon);color:#fff;font:500 5px "Oswald",sans-serif;display:flex;align-items:center;justify-content:center}
.list{font-size:3.4px;color:#444;line-height:1.5}
.list h4{font-size:4px;font-weight:600;color:var(--maroon)}
.member{position:absolute;text-align:center;font-size:2.6px;color:#777}
.member strong{display:block;color:var(--maroon);font-size:4px;font-weight:600;margin-top:2px}
.timeline{position:absolute;left:22px;right:22px;top:82px;height:.6px;background:var(--line)}
.dot{position:absolute;width:5px;height:5px;border-radius:50%;background:var(--maroon)}
.tag{position:absolute;background:var(--maroon);color:#fff;font-size:2.6px;padding:1px 2px}
.yr{position:absolute;font:300 10px "Oswald",sans-serif;color:#999}
.yr.s{font-size:4px;color:#555}
.pill{position:absolute;width:14px;height:14px;border-radius:50%;border:.6px solid #aaa;font-size:2.6px;display:flex;align-items:center;justify-content:center;color:#888;background:#fff}
.icon{position:absolute;text-align:center;font-size:2.6px;color:#555;width:36px}
.icon .c{width:15px;height:15px;border-radius:50%;margin:0 auto 3px;background:var(--maroon);display:flex;align-items:center;justify-content:center}
.icon .c.g{background:#b5b5b5}
.icon .c::after{content:"";width:6px;height:6px;background:#fff;border-radius:1px}
.panel{position:absolute;background:var(--maroon);color:#fff}
.gray{background:#55504d}
table{border-collapse:collapse;width:100%;font-size:2.4px}
th{background:var(--maroon);color:#fff;text-align:left;padding:1px 2px;font-weight:600}
td{padding:1.2px 2px;border-bottom:.4px solid #ddd;color:#666}
.seal{position:absolute;width:22px;height:22px;border-radius:50%;border:1.5px solid var(--maroon)}
.badge{position:absolute;width:30px;height:18px;background:#ececec;border:.5px solid #ccc}
.cap{position:absolute;font-size:2.4px;color:#666;text-align:center;width:30px}
</style>
</head>
<body>
<main class="deck">

<!-- 1 title -->
<section class="slide">
  <div class="ph bldg" style="inset:0;opacity:.25" role="img" aria-label="Faded building site backdrop"></div>
  <svg class="ph" style="inset:0" width="224" height="144"><polygon points="150,0 184,0 224,120 224,144 200,144" fill="#8a2a22"/></svg>
  <div class="brand big" style="left:40px;right:auto;top:62px"><b>MERIDIAN</b><i>Properties</i></div>
  <div class="ptitle" style="position:absolute;left:20px;top:104px">PRESENTATION TITLE HERE</div>
  <div class="bullets" style="position:absolute;left:20px;top:117px"><span>Building Construction</span><span>Civil Construction</span><span>Property Development</span></div>
  <div class="btn" style="position:absolute;left:24px;top:127px">SLIDE HERE</div>
</section>

<!-- 2 title -->
<section class="slide">
  <div class="ph bldg" style="inset:0;opacity:.35" role="img" aria-label="Faded photo of a commercial building"></div>
  <div class="brand big" style="left:0;right:0;top:48px"><b>MERIDIAN</b><i>Properties</i></div>
  <div class="ptitle" style="position:absolute;left:0;right:0;top:82px;text-align:center">PRESENTATION TITLE HERE</div>
  <div class="bullets" style="position:absolute;left:0;right:0;top:95px;justify-content:center"><span>Building Construction</span><span>Civil Construction</span><span>Property Development</span></div>
  <div style="position:absolute;left:0;right:0;top:106px;text-align:center"><span class="btn">SLIDE HERE</span></div>
</section>

<!-- 3 title -->
<section class="slide">
  <div class="brand big" style="left:0;right:0;top:6px"><b>MERIDIAN</b><i>Properties</i></div>
  <div class="ph soil" style="left:0;right:0;top:34px;height:70px" role="img" aria-label="Red soil road under construction lined with trees"></div>
  <div class="ptitle" style="position:absolute;left:0;right:0;top:111px;text-align:center">PRESENTATION TITLE HERE</div>
  <div class="bullets" style="position:absolute;left:0;right:0;top:124px;justify-content:center"><span>Building Construction</span><span>Civil Construction</span><span>Property Development</span></div>
  <div style="position:absolute;left:0;right:0;top:133px;text-align:center"><span class="btn">SLIDE HERE</span></div>
</section>

<!-- 4 agenda -->
<section class="slide">
  <div class="agenda-dark"><h3>AGENDA</h3><p class="txt"><b>Lorem ipsum</b><br>Lorem ipsum dolor sit amet, sed diam nonummy dolore magna aliquam erat.</p></div>
  <div class="panel" style="left:80px;top:0;bottom:0;width:52px;text-align:center;font:400 12px 'Oswald',sans-serif;padding-top:20px;line-height:1">
    18<br><span style="font-size:5px">DAY</span><br><br>08<br><span style="font-size:5px">MONTH</span><br><br>18<br><span style="font-size:5px">YEAR</span>
  </div>
  <div class="list" style="position:absolute;left:148px;top:24px">
    <h4>Review Q4</h4>• Q3 vs. Q4 Numbers<br>• Activity / Metrics<br>• Goal achievement<br><br>
    <h4>Review 2017</h4><br><h4>Performance Highlights</h4><br>
    <h4>2018 Plan</h4>• Q1<br>• YE<br>• Market Updates<br>• Effort &amp; Expectations
  </div>
</section>

<!-- 5 agenda numbered -->
<section class="slide">
  <div class="agenda-dark" style="width:76px;padding-left:16px"><h3>AGENDA</h3><p class="txt"><b>Lorem ipsum</b><br>Lorem ipsum dolor sit amet, sed diam nonummy dolore magna.</p></div>
  <div class="numbox" style="left:80px;top:48px">01</div>
  <div class="list" style="position:absolute;left:96px;top:40px"><h4>Review Q4</h4>• Q3 vs. Q4 Numbers<br>• Activity / Metrics<br>• Goal achievement</div>
  <div class="numbox" style="left:152px;top:48px">02</div>
  <div class="list" style="position:absolute;left:170px;top:50px"><h4>Review 2017</h4></div>
  <div class="numbox" style="left:80px;top:98px">03</div>
  <div class="list" style="position:absolute;left:96px;top:102px"><h4>Performance Highlights</h4></div>
  <div class="numbox" style="left:152px;top:98px">04</div>
  <div class="list" style="position:absolute;left:170px;top:84px"><h4>2018 Plan</h4>• Q1<br>• YE<br>• Market Updates<br>• Effort &amp; Expectations</div>
</section>

<!-- 6 welcome -->
<section class="slide">
  <div class="ph soil" style="left:0;right:0;top:0;height:72px" role="img" aria-label="Road works with red soil and construction machinery"></div>
  <div class="ph face" style="left:92px;top:50px;width:40px;height:40px;border-radius:50%;border:2px solid #fff" role="img" aria-label="Portrait of the managing director in a hard hat"></div>
  <div style="position:absolute;left:0;right:0;top:96px;text-align:center;font:500 9px 'Oswald',sans-serif;color:var(--maroon)">Welcome Message</div>
  <p class="txt" style="position:absolute;left:60px;right:60px;top:110px;text-align:center">Lorem ipsum dolor sit amet, consectetur adipiscing elit. Phasellus placerat massa odio eget rhoncus sapien congue id.</p>
</section>

<!-- 7 about -->
<section class="slide">
  <div class="title">About us</div><div class="brand"><b>MERIDIAN</b><i>Properties</i></div>
  <div class="ph face" style="left:16px;top:42px;width:54px;height:70px" role="img" aria-label="Portrait of the company founder"></div>
  <div class="tag" style="left:16px;top:106px">Your Name</div>
  <div style="position:absolute;left:90px;top:46px;font-size:5px;font-weight:700;color:var(--maroon)">Bio</div>
  <div class="txt" style="position:absolute;left:90px;top:56px;right:22px">Lorem ipsum dolor sit amet, consectetur adipiscing elit. Phasellus placerat massa odio, eget rhoncus sapien congue id. Etiam facilisis enim nulla.<br><br><span style="color:var(--maroon)">Donec venenatis tellus at tortor vestibulum, nec elementum neque tincidunt.</span><br><br>Lorem ipsum dolor sit amet, consectetur adipiscing elit. Phasellus placerat massa odio, eget rhoncus sapien congue id.<br><br><span style="color:var(--maroon)">Donec venenatis tellus at tortor vestibulum, nec elementum neque.</span></div>
  <div class="foot">www.yoursite.com</div>
</section>

<!-- 8 team 4 -->
<section class="slide">
  <div class="title">Our team</div><div class="brand"><b>MERIDIAN</b><i>Properties</i></div>
  <div class="member" style="left:16px;top:44px;width:40px"><div class="face" style="height:50px" role="img" aria-label="Team member portrait"></div><strong>Your Name</strong>Lorem ipsum dolor sit amet, consectetur adipiscing elit</div>
  <div class="member" style="left:66px;top:44px;width:40px"><div class="face2" style="height:50px" role="img" aria-label="Team member portrait"></div><strong>Your Name</strong>Lorem ipsum dolor sit amet, consectetur adipiscing elit</div>
  <div class="member" style="left:116px;top:44px;width:40px"><div class="face" style="height:50px" role="img" aria-label="Team member portrait"></div><strong>Your Name</strong>Lorem ipsum dolor sit amet, consectetur adipiscing elit</div>
  <div class="member" style="left:166px;top:44px;width:40px"><div class="face2" style="height:50px" role="img" aria-label="Team member portrait"></div><strong>Your Name</strong>Lorem ipsum dolor sit amet, consectetur adipiscing elit</div>
  <div class="foot">www.yoursite.com</div>
</section>

<!-- 9 team 8 -->
<section class="slide">
  <div class="title">Our team</div><div class="brand"><b>MERIDIAN</b><i>Properties</i></div>
  <div class="member" style="left:38px;top:32px;width:30px"><div class="face" style="height:38px" role="img" aria-label="Team member portrait"></div><strong>Your Name</strong>Lorem ipsum dolor</div>
  <div class="member" style="left:80px;top:32px;width:30px"><div class="face2" style="height:38px" role="img" aria-label="Team member portrait"></div><strong>Your Name</strong>Lorem ipsum dolor</div>
  <div class="member" style="left:122px;top:32px;width:30px"><div class="face" style="height:38px" role="img" aria-label="Team member portrait"></div><strong>Your Name</strong>Lorem ipsum dolor</div>
  <div class="member" style="left:164px;top:32px;width:30px"><div class="face2" style="height:38px" role="img" aria-label="Team member portrait"></div><strong>Your Name</strong>Lorem ipsum dolor</div>
  <div class="member" style="left:38px;top:88px;width:30px"><div class="face" style="height:38px" role="img" aria-label="Team member portrait"></div><strong>Your Name</strong>Lorem ipsum dolor</div>
  <div class="member" style="left:80px;top:88px;width:30px"><div class="face2" style="height:38px" role="img" aria-label="Team member portrait"></div><strong>Your Name</strong>Lorem ipsum dolor</div>
  <div class="member" style="left:122px;top:88px;width:30px"><div class="face" style="height:38px" role="img" aria-label="Team member portrait"></div><strong>Your Name</strong>Lorem ipsum dolor</div>
  <div class="member" style="left:164px;top:88px;width:30px"><div class="face2" style="height:38px" role="img" aria-label="Team member portrait"></div><strong>Your Name</strong>Lorem ipsum dolor</div>
  <div class="foot">www.yoursite.com</div>
</section>

<!-- 10 history -->
<section class="slide">
  <div class="title">Our history</div><div class="brand"><b>MERIDIAN</b><i>Properties</i></div>
  <p style="position:absolute;left:16px;right:16px;top:32px;font-size:3.4px;font-weight:600;color:var(--maroon);text-align:center">Established in March 2001, Meridian Properties is a highly acclaimed 100% black-owned construction and infrastructure development company built on a foundation of entrepreneurial excellence.</p>
  <div class="ph bldg" style="left:12px;top:54px;width:66px;height:70px" role="img" aria-label="Company head office building"></div>
  <div style="position:absolute;left:92px;top:54px;font:500 5px 'Oswald',sans-serif;color:var(--maroon)">JOURNEY</div>
  <svg class="ph" style="left:90px;top:62px" width="124" height="60" viewBox="0 0 124 60">
    <path d="M2 44 C30 44 60 36 80 24 S110 8 120 4" fill="none" stroke="#8a2a22" stroke-width=".8" stroke-dasharray="2 1"/>
    <g fill="#8a2a22"><circle cx="14" cy="44" r="1.5"/><circle cx="34" cy="42" r="1.5"/><circle cx="54" cy="38" r="1.5"/><circle cx="74" cy="28" r="1.5"/><circle cx="94" cy="18" r="1.5"/><circle cx="114" cy="6" r="1.5"/></g>
    <g font-size="2.6" fill="#fff" font-family="Open Sans"><rect x="8" y="32" width="10" height="3" fill="#8a2a22"/><text x="9" y="34.5">1997</text><rect x="28" y="48" width="10" height="3" fill="#8a2a22"/><text x="29" y="50.5">2001</text><rect x="48" y="26" width="10" height="3" fill="#8a2a22"/><text x="49" y="28.5">2003</text><rect x="70" y="34" width="10" height="3" fill="#8a2a22"/><text x="71" y="36.5">2006</text><rect x="88" y="6" width="10" height="3" fill="#8a2a22"/><text x="89" y="8.5">2011</text><rect x="108" y="14" width="10" height="3" fill="#8a2a22"/><text x="109" y="16.5">2017</text></g>
  </svg>
  <div class="foot">www.yoursite.com</div>
</section>

<!-- 11 journey -->
<section class="slide">
  <div class="title">Our journey</div><div class="brand"><b>MERIDIAN</b><i>Properties</i></div>
  <div class="timeline"></div>
  <div class="pill" style="left:22px;top:75px">START</div>
  <div class="yr s" style="left:68px;top:42px">1980</div><div class="tag" style="left:68px;top:50px">AGENDA GOES HERE</div>
  <div class="txt" style="position:absolute;left:68px;top:57px;width:40px;font-size:2.6px">Lorem ipsum dolor sit amet, consectetur adipiscing</div>
  <div class="yr" style="left:126px;top:48px">1990</div>
  <div class="yr s" style="left:164px;top:42px">1993</div><div class="tag" style="left:164px;top:50px">AGENDA GOES HERE</div>
  <div class="dot" style="left:68px;top:80px"></div><div class="dot" style="left:118px;top:80px"></div><div class="dot" style="left:166px;top:80px"></div>
  <div class="yr s" style="left:118px;top:92px">1990</div><div class="tag" style="left:118px;top:100px">AGENDA GOES HERE</div>
  <div class="yr" style="left:66px;top:104px">1980</div><div class="yr" style="left:184px;top:104px">1993</div>
  <div class="foot">www.yoursite.com</div>
</section>

<!-- 12 journey -->
<section class="slide">
  <div class="title">Our journey</div><div class="brand"><b>MERIDIAN</b><i>Properties</i></div>
  <div class="timeline" style="left:0;right:0"></div>
  <div class="yr s" style="left:36px;top:42px">1994</div><div class="tag" style="left:36px;top:50px">AGENDA GOES HERE</div>
  <div class="yr" style="left:110px;top:48px">1997</div>
  <div class="yr s" style="left:162px;top:42px">1998</div><div class="tag" style="left:162px;top:50px">AGENDA GOES HERE</div>
  <div class="dot" style="left:38px;top:80px"></div><div class="dot" style="left:104px;top:80px"></div><div class="dot" style="left:164px;top:80px"></div>
  <div class="yr s" style="left:100px;top:92px">1997</div><div class="tag" style="left:100px;top:100px">AGENDA GOES HERE</div>
  <div class="yr" style="left:48px;top:104px">1994</div><div class="yr" style="left:168px;top:104px">1998</div>
  <div class="foot">www.yoursite.com</div>
</section>

<!-- 13 journey -->
<section class="slide">
  <div class="title">Our journey</div><div class="brand"><b>MERIDIAN</b><i>Properties</i></div>
  <div class="timeline" style="left:0;right:22px"></div>
  <div class="pill" style="left:188px;top:75px">FINISH</div>
  <div class="yr s" style="left:36px;top:42px">2000</div><div class="tag" style="left:36px;top:50px">AGENDA GOES HERE</div>
  <div class="yr" style="left:110px;top:48px">2005</div>
  <div class="dot" style="left:38px;top:80px"></div><div class="dot" style="left:104px;top:80px"></div>
  <div class="yr s" style="left:100px;top:92px">2005</div><div class="tag" style="left:100px;top:100px">AGENDA GOES HERE</div>
  <div class="yr" style="left:50px;top:104px">2000</div>
  <div class="foot">www.yoursite.com</div>
</section>

<!-- 14 mission -->
<section class="slide">
  <div class="title">Our mission &amp; vision</div><div class="brand"><b>MERIDIAN</b><i>Properties</i></div>
  <div class="panel" style="left:0;right:0;top:36px;height:84px"></div>
  <div style="position:absolute;left:22px;top:46px;width:54px;color:#fff"><div style="font-size:4px;margin-bottom:3px">Our Vision</div><div class="txt" style="color:#f0d9d6;font-size:2.6px">Our vision is to be a world-class black-owned construction company recognised for quality, integrity and the wellbeing of the communities we serve.</div></div>
  <div style="position:absolute;left:80px;top:46px;width:54px;color:#fff"><div style="font-size:4px;margin-bottom:3px">Our Mission</div><div class="txt" style="color:#f0d9d6;font-size:2.6px">Our mission is to develop significant partnerships, deliver projects on time and empower our people, clients and communities through sustainable growth and excellence.</div></div>
  <div class="ph suit" style="left:156px;top:22px;width:54px;height:122px" role="img" aria-label="Businessman in a navy suit"></div>
  <div class="foot">www.yoursite.com</div>
</section>

<!-- 15 services -->
<section class="slide">
  <div class="title">Our service</div><div class="brand"><b>MERIDIAN</b><i>Properties</i></div>
  <div class="icon" style="left:20px;top:42px"><div class="c"></div>Residential Buildings</div>
  <div class="icon" style="left:66px;top:42px"><div class="c g"></div>Commercial Buildings</div>
  <div class="icon" style="left:112px;top:42px"><div class="c"></div>Public Buildings</div>
  <div class="icon" style="left:158px;top:42px"><div class="c g"></div>Civil Construction</div>
  <div class="icon" style="left:20px;top:90px"><div class="c"></div>Roads &amp; Earthworks</div>
  <div class="icon" style="left:66px;top:90px"><div class="c g"></div>Water &amp; Sanitation</div>
  <div class="icon" style="left:112px;top:90px"><div class="c"></div>Civil Structures</div>
  <div class="icon" style="left:158px;top:90px"><div class="c g"></div>Property Development</div>
  <div class="foot">www.yoursite.com</div>
</section>

<!-- 16 values -->
<section class="slide">
  <div class="title">Our values</div><div class="brand"><b>MERIDIAN</b><i>Properties</i></div>
  <svg class="ph" style="left:24px;top:60px" width="64" height="60" viewBox="0 0 64 60" font-family="Oswald" font-size="7" fill="#fff" text-anchor="middle">
    <g transform="rotate(45 32 30)"><rect x="14" y="12" width="15" height="15" fill="#8a2a22"/><rect x="31" y="12" width="15" height="15" fill="#6e1f19"/><rect x="14" y="29" width="15" height="15" fill="#6e1f19"/><rect x="31" y="29" width="15" height="15" fill="#8a2a22"/></g>
    <text x="20" y="31">P</text><text x="32" y="19">A</text><text x="44" y="31">T</text><text x="32" y="43">H</text>
  </svg>
  <p class="txt" style="position:absolute;left:104px;top:36px;right:22px;font-size:2.8px">In pursuit of our vision and mission, our values outline the PATH to our growth into a housing and infrastructure development company that places our clients at the forefront of all our interventions.</p>
  <div class="icon" style="left:112px;top:72px"><div class="c"></div>Professionalism</div>
  <div class="icon" style="left:160px;top:72px"><div class="c"></div>Accountability</div>
  <div class="icon" style="left:112px;top:102px"><div class="c"></div>Transparency</div>
  <div class="icon" style="left:160px;top:102px"><div class="c"></div>Honesty</div>
  <div class="foot">www.yoursite.com</div>
</section>

<!-- 17 residential -->
<section class="slide">
  <div class="title red">Residential buildings</div><div class="brand"><b>MERIDIAN</b><i>Properties</i></div>
  <p class="txt" style="position:absolute;left:16px;right:16px;top:38px">From inception, Meridian Properties' work with residential buildings has been renowned and nationally recognised. We have built communities and contributed to provincial and state housing infrastructure initiatives by successfully completing low-cost projects.<br><br>Reconstruction and Development Programme housing projects and walk-up houses as well as buildings for the national, provincial and municipal governments in South Africa.<br><span style="color:var(--maroon);font-weight:700;display:block;text-align:center">RESIDENTIAL BUILDINGS</span></p>
  <div class="ph bldg" style="left:16px;top:90px;width:62px;height:38px" role="img" aria-label="Multi-storey residential block"></div>
  <div class="ph site" style="left:81px;top:90px;width:62px;height:38px" role="img" aria-label="Houses on a hillside"></div>
  <div class="ph bldg" style="left:146px;top:90px;width:62px;height:38px" role="img" aria-label="Modern residential house"></div>
  <div class="foot">www.yoursite.com</div>
</section>

<!-- 18 commercial -->
<section class="slide">
  <div class="brand"><b>MERIDIAN</b><i>Properties</i></div>
  <div class="ph bldg" style="left:0;top:0;width:88px;height:144px" role="img" aria-label="Tall commercial building under blue sky"></div>
  <div style="position:absolute;left:100px;top:30px;font:500 6px 'Oswald',sans-serif;color:var(--maroon);line-height:1.2">COMMERCIAL AND<br>INDUSTRIAL BUILDINGS</div>
  <p class="txt" style="position:absolute;left:100px;right:12px;top:52px;font-size:2.8px">As a company, Meridian Properties continues to raise the standard in the development of commercial and industrial infrastructure. Office blocks, factories, shopping malls, warehouses and steel structures in different provinces.</p>
  <div class="ph site" style="left:100px;top:92px;width:50px;height:38px" role="img" aria-label="Building site with scaffolding"></div>
  <div class="ph bldg" style="left:156px;top:92px;width:54px;height:38px" role="img" aria-label="Completed commercial facade"></div>
  <div class="foot" style="left:88px">www.yoursite.com</div>
</section>

<!-- 19 public -->
<section class="slide">
  <div class="title red">Service and public buildings</div><div class="brand"><b>MERIDIAN</b><i>Properties</i></div>
  <div class="ph bldg" style="left:0;top:38px;width:54px;height:46px" role="img" aria-label="Public school buildings"></div>
  <div class="ph soil" style="left:56px;top:38px;width:54px;height:46px" role="img" aria-label="Courtyard of a public building"></div>
  <div class="ph bldg" style="left:116px;top:30px;width:84px;height:62px" role="img" aria-label="Government office building at dusk"></div>
  <p class="txt" style="position:absolute;left:90px;right:12px;top:96px;font-size:2.8px">Meridian Properties has become a trusted name in the construction of service and public buildings throughout South Africa, including schools, technical colleges, government buildings, hospitals and clinics, built to the highest standard.</p>
  <div class="foot">www.yoursite.com</div>
</section>

<!-- 20 roads -->
<section class="slide">
  <div class="title red">Roads and earthworks</div><div class="brand"><b>MERIDIAN</b><i>Properties</i></div>
  <div class="ph road" style="left:12px;top:34px;width:70px;height:50px" role="img" aria-label="Traffic on a newly built road"></div>
  <div class="ph road" style="left:84px;top:34px;width:70px;height:50px" role="img" aria-label="Freshly marked road lanes"></div>
  <div class="ph site" style="left:12px;top:86px;width:70px;height:48px" role="img" aria-label="Earthworks with excavators"></div>
  <div class="ph road" style="left:84px;top:86px;width:70px;height:48px" role="img" aria-label="Rapid transit lane construction"></div>
  <p class="txt" style="position:absolute;left:160px;right:10px;top:34px;font-size:2.7px">Over the years Meridian Properties has successfully completed a number of roads and earthworks projects including the bus rapid transit systems and roadworks as well as other road and highway construction projects around South Africa.<br><br>Our experience and capacity deliver excellent service in high-value civil construction projects.</p>
  <div class="foot">www.yoursite.com</div>
</section>

<!-- 21 water -->
<section class="slide">
  <div class="title red">Water and sanitation</div><div class="brand"><b>MERIDIAN</b><i>Properties</i></div>
  <p class="txt" style="position:absolute;left:16px;top:34px;width:110px;font-size:2.7px">Meridian Properties is renowned for delivering on large-scale water and sanitation projects including pipeline extensions, excavations, water supply systems, reticulation, sewer infrastructure and toilet eradication systems. Our proficiency continues to grow as we innovatively upskill our workforce.</p>
  <div class="ph pipe" style="left:146px;top:34px;width:60px;height:50px" role="img" aria-label="Blue pipeline laid in a trench"></div>
  <div class="ph soil" style="left:22px;top:90px;width:40px;height:40px" role="img" aria-label="Workers in an excavation"></div>
  <div class="ph soil" style="left:66px;top:90px;width:60px;height:40px" role="img" aria-label="Excavator on red earth"></div>
  <div class="ph pipe" style="left:130px;top:90px;width:70px;height:40px" role="img" aria-label="Pipe installation crew"></div>
  <div class="foot">www.yoursite.com</div>
</section>

<!-- 22 civil -->
<section class="slide">
  <div class="title red">Civil structures</div><div class="brand"><b>MERIDIAN</b><i>Properties</i></div>
  <div class="ph site" style="left:0;top:40px;width:50px;height:92px" role="img" aria-label="Reservoir construction"></div>
  <div class="ph site" style="left:54px;top:30px;width:56px;height:102px" role="img" aria-label="Concrete formwork and rebar"></div>
  <div class="ph bldg" style="left:114px;top:36px;width:50px;height:96px" role="img" aria-label="Bridge structure under construction"></div>
  <p class="txt" style="position:absolute;left:170px;right:8px;top:30px;font-size:2.6px">Meridian Properties is an expert civil structure construction company. We have earned our place in the top ranks of leading bridge, dam and reservoir construction companies in South Africa by our skilful delivery of civil structure projects. Our capacity in this field allows us to build reservoirs, water treatment plants and civil infrastructure.</p>
  <div class="foot">www.yoursite.com</div>
</section>

<!-- 23 property -->
<section class="slide">
  <div class="title red">Property development</div><div class="brand"><b>MERIDIAN</b><i>Properties</i></div>
  <div class="ph bldg" style="left:12px;top:40px;width:54px;height:40px" role="img" aria-label="Townhouse development"></div>
  <div class="ph bldg" style="left:68px;top:40px;width:40px;height:40px" role="img" aria-label="Modern apartment block"></div>
  <div class="ph bldg" style="left:12px;top:84px;width:54px;height:40px" role="img" aria-label="Residential complex"></div>
  <div class="ph soil" style="left:70px;top:84px;width:86px;height:40px" role="img" aria-label="Brick housing estate"></div>
  <p class="txt" style="position:absolute;left:118px;right:16px;top:40px;font-size:2.8px">Meridian Properties is proficient in turnkey property development solutions. We work our way through the property development value chain, from land procurement, property zoning and the concept proposal to architectural designs and the actual building and development of the housing.</p>
  <div class="foot">www.yoursite.com</div>
</section>

<!-- 24 featured -->
<section class="slide">
  <div class="title red">Featured construction projects</div><div class="brand"><b>MERIDIAN</b><i>Properties</i></div>
  <svg class="ph" style="left:12px;top:30px" width="204" height="108" viewBox="0 0 204 108">
    <defs><linearGradient id="thumb" x1="0" y1="0" x2="0" y2="1"><stop offset="0" stop-color="#a9c1d8"/><stop offset=".5" stop-color="#b07a58"/><stop offset="1" stop-color="#6b5a50"/></linearGradient></defs>
    <g fill="url(#thumb)"><rect x="0" y="0" width="36" height="22"/><rect x="41" y="0" width="36" height="22"/><rect x="82" y="0" width="36" height="22"/><rect x="123" y="0" width="36" height="22"/><rect x="164" y="0" width="36" height="22"/>
    <rect x="0" y="54" width="36" height="22"/><rect x="41" y="54" width="36" height="22"/><rect x="82" y="54" width="36" height="22"/><rect x="123" y="54" width="36" height="22"/><rect x="164" y="54" width="36" height="22"/></g>
    <g fill="#8a2a22"><rect x="0" y="25" width="18" height="1.6"/><rect x="41" y="25" width="18" height="1.6"/><rect x="82" y="25" width="18" height="1.6"/><rect x="123" y="25" width="18" height="1.6"/><rect x="164" y="25" width="18" height="1.6"/><rect x="0" y="79" width="18" height="1.6"/><rect x="41" y="79" width="18" height="1.6"/><rect x="82" y="79" width="18" height="1.6"/><rect x="123" y="79" width="18" height="1.6"/><rect x="164" y="79" width="18" height="1.6"/></g>
    <g fill="#ccc"><rect x="0" y="29" width="32" height="1"/><rect x="0" y="33" width="28" height="1"/><rect x="0" y="37" width="30" height="1"/><rect x="41" y="29" width="32" height="1"/><rect x="41" y="33" width="28" height="1"/><rect x="41" y="37" width="30" height="1"/><rect x="82" y="29" width="32" height="1"/><rect x="82" y="33" width="28" height="1"/><rect x="82" y="37" width="30" height="1"/><rect x="123" y="29" width="32" height="1"/><rect x="123" y="33" width="28" height="1"/><rect x="123" y="37" width="30" height="1"/><rect x="164" y="29" width="32" height="1"/><rect x="164" y="33" width="28" height="1"/><rect x="164" y="37" width="30" height="1"/>
    <rect x="0" y="83" width="32" height="1"/><rect x="0" y="87" width="28" height="1"/><rect x="41" y="83" width="32" height="1"/><rect x="41" y="87" width="28" height="1"/><rect x="82" y="83" width="32" height="1"/><rect x="82" y="87" width="28" height="1"/><rect x="123" y="83" width="32" height="1"/><rect x="123" y="87" width="28" height="1"/><rect x="164" y="83" width="32" height="1"/><rect x="164" y="87" width="28" height="1"/></g>
  </svg>
  <div class="foot">www.yoursite.com</div>
</section>

<!-- 25 gallery -->
<section class="slide">
  <div class="title red">Gallery</div><div class="brand"><b>MERIDIAN</b><i>Properties</i></div>
  <div class="ph bldg" style="left:16px;top:40px;width:82px;height:52px" role="img" aria-label="Apartment block with blue accent"></div>
  <div class="ph bldg" style="left:126px;top:40px;width:82px;height:52px" role="img" aria-label="Office building at dusk"></div>
  <div class="txt" style="position:absolute;left:16px;top:96px;width:90px;font-size:2.7px"><b style="color:var(--maroon)">Lorem ipsum</b><br>• Phasellus placerat massa odio, eget rhoncus sapien congue id.<br>• Etiam facilisis enim nulla, a sollicitudin tellus venenatis.</div>
  <div class="txt" style="position:absolute;left:126px;top:96px;width:90px;font-size:2.7px"><b style="color:var(--maroon)">Lorem ipsum</b><br>• Phasellus placerat massa odio, eget rhoncus sapien congue id.<br>• Donec venenatis tellus at tortor vestibulum.</div>
  <div class="foot">www.yoursite.com</div>
</section>

<!-- 26 gallery grid -->
<section class="slide">
  <div class="title red">Gallery</div><div class="brand"><b>MERIDIAN</b><i>Properties</i></div>
  <div class="ph soil" style="left:16px;top:36px;width:48px;height:40px" role="img" aria-label="Earthworks site"></div>
  <div class="panel" style="left:64px;top:36px;width:54px;height:40px;padding:4px"><p class="txt" style="color:#fff;font-size:2.8px">Donec venenatis tellus at tortor vestibulum, nec elementum neque tincidunt.</p></div>
  <div class="ph road" style="left:118px;top:36px;width:50px;height:40px" role="img" aria-label="Road with traffic"></div>
  <div class="panel gray" style="left:168px;top:36px;width:44px;height:40px;padding:4px"><p class="txt" style="color:#fff;font-size:2.8px">Donec venenatis tellus at tortor vestibulum, nec elementum neque.</p></div>
  <div class="panel gray" style="left:16px;top:76px;width:48px;height:40px;padding:4px"><p class="txt" style="color:#fff;font-size:2.8px">Donec venenatis tellus at tortor vestibulum, nec elementum neque.</p></div>
  <div class="ph bldg" style="left:64px;top:76px;width:54px;height:40px" role="img" aria-label="Row of townhouses"></div>
  <div class="panel" style="left:118px;top:76px;width:50px;height:40px;padding:4px"><p class="txt" style="color:#fff;font-size:2.8px">Donec venenatis tellus at tortor vestibulum, nec elementum neque.</p></div>
  <div class="ph bldg" style="left:168px;top:76px;width:44px;height:40px" role="img" aria-label="Office tower"></div>
  <div class="foot">www.yoursite.com</div>
</section>

<!-- 27 gallery mix -->
<section class="slide">
  <div class="title red">Gallery</div><div class="brand"><b>MERIDIAN</b><i>Properties</i></div>
  <div class="ph bldg" style="left:26px;top:36px;width:90px;height:46px" role="img" aria-label="School buildings"></div>
  <div class="panel" style="left:120px;top:36px;width:40px;height:96px;padding:5px"><div style="font:400 7px 'Oswald',sans-serif;line-height:1.1">Lorem<br>ipsum<br>dolor</div><p class="txt" style="color:#f0d9d6;font-size:2.6px;margin-top:3px">Lorem ipsum dolor sit amet, consectetur adipiscing elit. Phasellus placerat massa odio, eget rhoncus sapien congue id.</p></div>
  <div class="ph bldg" style="left:166px;top:36px;width:40px;height:46px" role="img" aria-label="Building facade"></div>
  <div class="ph site" style="left:26px;top:86px;width:44px;height:46px" role="img" aria-label="Steel structure"></div>
  <div class="ph site" style="left:72px;top:86px;width:44px;height:46px" role="img" aria-label="Construction workers"></div>
  <div class="ph bldg" style="left:166px;top:86px;width:40px;height:46px" role="img" aria-label="Apartment block"></div>
  <div class="foot">www.yoursite.com</div>
</section>

<!-- 28 gallery slide title -->
<section class="slide">
  <div class="title red">Gallery</div><div class="brand"><b>MERIDIAN</b><i>Properties</i></div>
  <div class="ph site" style="left:18px;top:42px;width:54px;height:40px" role="img" aria-label="Aerial view of housing site"></div>
  <div class="panel" style="left:70px;top:42px;width:92px;height:40px;padding:6px"><div style="font:400 7px 'Oswald',sans-serif">Slide Title Here</div><p class="txt" style="color:#f0d9d6;font-size:2.6px;margin-top:2px">Lorem ipsum dolor sit amet, consectetur adipiscing elit.</p></div>
  <div class="ph bldg" style="left:164px;top:42px;width:44px;height:40px" role="img" aria-label="Townhouses"></div>
  <div class="ph bldg" style="left:18px;top:86px;width:68px;height:44px" role="img" aria-label="Residential complex"></div>
  <div class="ph pipe" style="left:88px;top:86px;width:62px;height:44px" role="img" aria-label="Pipeline trench"></div>
  <div class="ph bldg" style="left:152px;top:86px;width:56px;height:44px" role="img" aria-label="Modern apartments"></div>
  <div class="foot">www.yoursite.com</div>
</section>

<!-- 29 road panel -->
<section class="slide">
  <div class="ph road" style="inset:0" role="img" aria-label="New road with lane arrows and a traffic cone"></div>
  <div class="panel" style="left:36px;top:0;width:58px;height:122px;padding:16px 8px">
    <div class="brand white" style="position:static;text-align:left"><b style="font-size:8px">MERIDIAN</b><i style="font-size:5px">Properties</i></div>
    <p class="txt" style="color:#f0d9d6;font-size:2.8px;margin-top:44px">Donec venenatis tellus at tortor vestibulum, nec elementum neque tincidunt.</p>
  </div>
</section>

<!-- 30 house panel -->
<section class="slide">
  <div class="ph soil" style="inset:0" role="img" aria-label="Brick house with paved driveway"></div>
  <div class="panel" style="left:128px;top:0;width:58px;height:144px;padding:18px 8px">
    <div class="brand white" style="position:static;text-align:left"><b style="font-size:8px">MERIDIAN</b><i style="font-size:5px">Properties</i></div>
    <p class="txt" style="color:#f0d9d6;font-size:2.8px;margin-top:72px">Donec venenatis tellus at tortor vestibulum, nec elementum neque tincidunt.</p>
  </div>
</section>

<!-- 31 lorem -->
<section class="slide">
  <div class="ph bldg" style="inset:0" role="img" aria-label="Office building against a blue sky"></div>
  <svg class="ph" style="inset:0" width="224" height="144"><polygon points="0,0 90,0 150,144 0,144" fill="#8a2a22" opacity=".92"/></svg>
  <div class="brand white" style="left:12px;right:auto;top:18px;text-align:left"><b style="font-size:8px">MERIDIAN</b><i style="font-size:5px">Properties</i></div>
  <div style="position:absolute;left:16px;top:92px;color:#fff;font:400 7px 'Oswald',sans-serif;line-height:1">Lorem<br><span style="font-size:4.5px">ipsum dolor sit amet</span></div>
  <p class="txt" style="position:absolute;left:16px;top:110px;width:90px;color:#f0d9d6;font-size:2.6px"><b>Lorem ipsum</b> is simply dummy text of the printing and typesetting industry. Lorem ipsum has been the industry's standard dummy text ever since the 1500s.</p>
</section>

<!-- 32 portfolio -->
<section class="slide">
  <div class="title red">Building construction portfolio</div><div class="brand"><b>MERIDIAN</b><i>Properties</i></div>
  <div style="position:absolute;left:20px;right:16px;top:28px">
    <div style="font-size:3px;font-weight:700;color:var(--maroon);margin-bottom:2px">SCHOOLS CONSTRUCTION</div>
    <table><tr><th>PROJECT NR</th><th>DESCRIPTION</th><th>CLIENT</th></tr>
      <tr><td>SCH-01</td><td>Construction of a secondary school, phase one</td><td>Department of Public Works</td></tr>
      <tr><td>SCH-02</td><td>Upgrading of classrooms and laboratories</td><td>Department of Public Works</td></tr>
      <tr><td>SCH-03</td><td>Construction of a primary school and hall</td><td>Department of Education</td></tr>
      <tr><td>SCH-04</td><td>Sanitation facilities at rural schools</td><td>Department of Education</td></tr>
      <tr><td>SCH-05</td><td>New technical college workshop block</td><td>Department of Public Works</td></tr></table>
    <div style="font-size:3px;font-weight:700;color:var(--maroon);margin:4px 0 2px">HOSPITALS AND CLINICS CONSTRUCTION</div>
    <table><tr><th>PROJECT NR</th><th>DESCRIPTION</th><th>CLIENT</th></tr>
      <tr><td>HSP-01</td><td>New district hospital outpatient wing</td><td>Department of Health</td></tr>
      <tr><td>HSP-02</td><td>Community clinic construction</td><td>Department of Health</td></tr>
      <tr><td>HSP-03</td><td>Hospital maintenance and upgrades</td><td>Department of Health</td></tr></table>
  </div>
  <div class="foot">www.yoursite.com</div>
</section>

<!-- 33 awards -->
<section class="slide">
  <div class="title red">Accreditation and awards</div><div class="brand"><b>MERIDIAN</b><i>Properties</i></div>
  <div class="badge" style="left:22px;top:46px"></div>
  <div class="badge" style="left:64px;top:46px"></div>
  <div class="badge" style="left:106px;top:46px"></div>
  <div class="badge" style="left:148px;top:46px"></div>
  <div class="seal" style="left:28px;top:80px"></div>
  <div class="seal" style="left:60px;top:80px"></div>
  <div class="seal" style="left:92px;top:80px"></div>
  <div class="seal" style="left:124px;top:80px"></div>
  <div class="seal" style="left:156px;top:80px"></div>
  <div class="cap" style="left:24px;top:106px">National Housing Developer of the Year</div>
  <div class="cap" style="left:56px;top:106px">Certificate of Appreciation</div>
  <div class="cap" style="left:88px;top:106px">Contractor of the Year</div>
  <div class="cap" style="left:120px;top:106px">Housing Developer of the Year</div>
  <div class="cap" style="left:152px;top:106px">Contractor of the Year Provincial</div>
  <div class="foot">www.yoursite.com</div>
</section>

<!-- 34 social -->
<section class="slide">
  <div class="title red">Social responsibility</div><div class="brand"><b>MERIDIAN</b><i>Properties</i></div>
  <div style="position:absolute;left:16px;top:48px;width:40px;text-align:center"><div style="width:14px;height:14px;background:var(--maroon);margin:0 auto 3px"></div><div style="font-size:3.4px;color:var(--maroon);font-weight:600">Stonehill Foundation</div></div>
  <div style="position:absolute;left:66px;right:14px;top:30px">
    <div style="font-size:3px;font-weight:700;color:var(--maroon)">STONEHILL FOUNDATION</div>
    <p class="txt" style="font-size:2.6px">Meridian Properties currently directs all of its corporate social initiatives towards the Stonehill Foundation. The objective of the foundation is to advance education, support communities and uplift the youth through targeted programmes and partnerships.</p>
    <div style="font-size:3px;font-weight:700;color:var(--maroon);margin-top:4px">FOUNDATION PROJECTS</div>
    <div style="display:flex;gap:6px"><p class="txt" style="font-size:2.5px;flex:1"><b style="color:var(--maroon)">Educational Donations</b><br>Donations of school uniforms, stationery and learning materials to learners in need.<br><b style="color:var(--maroon)">Entrepreneurship Programme</b><br>Skills development for emerging contractors.</p>
    <p class="txt" style="font-size:2.5px;flex:1"><b style="color:var(--maroon)">Community Day</b><br>Volunteers build and refurbish homes for vulnerable families.<br><b style="color:var(--maroon)">Church Support</b><br>Contribution towards community church facilities.</p></div>
  </div>
  <div class="foot">www.yoursite.com</div>
</section>

<!-- 35 thank you -->
<section class="slide">
  <div class="ph hand" style="left:0;right:0;top:0;height:104px" role="img" aria-label="Hand signing a document with a pen"></div>
  <div style="position:absolute;left:12px;top:18px;color:#fff;font:500 11px 'Oswald',sans-serif">THANK YOU</div>
  <p style="position:absolute;left:12px;top:35px;width:110px;color:#fff;font-size:4px;line-height:1.3">We're excited to hear about your goals and how we can help you achieve them.</p>
  <div class="panel" style="left:0;right:0;top:104px;bottom:0;padding:4px 8px;display:flex;gap:8px;font-size:2.4px;line-height:1.4">
    <div><b>HEAD OFFICE</b><br>12 Ridge Road<br>Midrand 1685<br>Tel: +27 11 000 0000</div>
    <div><b>PRETORIA OFFICE</b><br>48 Park Street<br>Hatfield 0083<br>Tel: +27 12 000 0000</div>
    <div><b>POLOKWANE OFFICE</b><br>7 Market Lane<br>Polokwane 0699<br>Tel: +27 15 000 0000</div>
    <div class="brand white" style="position:static;margin-left:auto;align-self:center"><b style="font-size:8px">MERIDIAN</b><i style="font-size:5px">Properties</i></div>
  </div>
</section>

</main>
</body>
</html>
```